Postcard Design

I have an accounting firm and I would like to increase my customer base by a postcard mailout/letter dropI want a design that is eye catching and uses my logo. I specialise in small to medium business and offer services for commercial accounting and business advisory. I also want to offer a discount for new clients.Previously I had my website updated and would like to stay with the theme

Industry/Entity Type

Business Consultant

Font styles to use
Serif

Colors
b667aa
d3a5cc

Requirements
Must have
• the post card needs to be arty to attract attention. also business like

```html
<!DOCTYPE html>
<html lang="en">
<head>
<meta charset="utf-8">
<title>Accounting Postcard – Front and Back</title>
<link rel="stylesheet" href="https://fonts.googleapis.com/css2?family=Fira+Sans+Condensed:wght@400;500;600&family=Jost:wght@300;400&display=swap">
<style>
  :root {
    --navy: #2a3950;
    --red: #a51e23;
    --teal: #3aa79a;
    --deep-green: #1f5e51;
    --white: #ffffff;
    --ink: #1a1a1a;
    --photo-light: #e6ecf0;
    --photo-mid: #aebdc8;
    --rule: #333333;
  }
  * { margin: 0; padding: 0; box-sizing: border-box; }
  html, body {
    width: 1200px; height: 929px; overflow: hidden;
    background: var(--white);
  }
  .canvas { position: relative; width: 1200px; height: 929px; }
  .postcard {
    position: absolute; width: 502px; height: 388px;
    background: var(--white);
    box-shadow: 0 8px 28px rgba(0,0,0,0.28);
    overflow: hidden;
  }
  .postcard--front { left: 113px; top: 73px; }
  .postcard--back { left: 615px; top: 462px; }
  .postcard__art { position: absolute; inset: 0; width: 502px; height: 388px; }

  .pitch {
    position: absolute; left: 18px; top: 245px; width: 320px;
    font-family: "Fira Sans Condensed", sans-serif; font-weight: 500;
    font-size: 16.5px; line-height: 19px; color: var(--ink);
  }
  .offer {
    position: absolute; right: 28px; top: 316px;
    font-family: "Fira Sans Condensed", sans-serif; font-weight: 600;
    font-size: 16px; color: var(--white);
  }
  .contact-bar {
    position: absolute; left: 0; right: 0; bottom: 0; height: 51px;
    display: flex; align-items: center; justify-content: center;
    font-family: "Jost", sans-serif; font-weight: 300;
    font-size: 17px; color: var(--white); letter-spacing: 0.2px;
  }

  .logo-box {
    position: absolute; left: 29px; top: 21px; width: 148px; height: 132px;
    background: var(--white); border: 1.5px solid var(--rule);
    display: flex; align-items: center; justify-content: center;
    font-family: "Fira Sans Condensed", sans-serif; font-weight: 400;
    font-size: 20px; color: var(--ink);
  }
  .stamp-box {
    position: absolute; left: 385px; top: 24px; width: 81px; height: 71px;
    border: 1px solid var(--rule);
    font-family: "Fira Sans Condensed", sans-serif; font-size: 16px;
    text-align: center; padding-top: 24px; color: var(--ink);
  }
  .company-details {
    position: absolute; left: 36px; top: 188px; width: 120px;
    font-family: "Fira Sans Condensed", sans-serif; font-size: 16px;
    line-height: 24px; color: var(--ink);
  }
  .company-details p + p { margin-top: 14px; }
  .address-lines { position: absolute; left: 237px; top: 153px; width: 233px; }
  .address-lines span {
    display: block; height: 1px; background: var(--rule); margin-bottom: 20px;
  }
</style>
</head>
<body>
<main class="canvas">

  <section class="postcard postcard--front" aria-label="Postcard front">
    <svg class="postcard__art" viewBox="0 0 502 388" aria-hidden="false">
      <defs>
        <linearGradient id="photoTone" x1="0" y1="0" x2="0" y2="1">
          <stop offset="0" stop-color="var(--photo-mid)"/>
          <stop offset="0.6" stop-color="var(--photo-light)"/>
          <stop offset="1" stop-color="var(--white)"/>
        </linearGradient>
      </defs>
      <polygon points="0,0 502,0 502,8 0,80" fill="var(--navy)"/>
      <g role="img" aria-label="Photo of business people working with a calculator, pen and financial charts">
        <polygon points="0,80 502,8 502,235 0,235" fill="url(#photoTone)"/>
      </g>
      <polygon points="342,0 502,0 502,167" fill="var(--red)"/>
      <polygon points="125,337 502,245 502,337" fill="var(--deep-green)"/>
      <polygon points="185,337 502,256 502,337" fill="var(--teal)"/>
      <rect x="0" y="337" width="502" height="51" fill="var(--navy)"/>
    </svg>
    <p class="pitch">We are specialise in small to medium business and offer services for commercial accounting and business advisory.</p>
    <p class="offer">Offer a discount for new clients.</p>
    <p class="contact-bar">Contact details: 1234567890 1234567890 www.ledgr.co</p>
  </section>

  <section class="postcard postcard--back" aria-label="Postcard back">
    <svg class="postcard__art" viewBox="0 0 502 388" aria-hidden="true">
      <polygon points="0,0 402,0 0,80" fill="var(--navy)"/>
      <polygon points="255,338 502,272 502,338" fill="var(--deep-green)"/>
      <polygon points="300,338 502,277 502,338" fill="var(--teal)"/>
      <rect x="0" y="338" width="502" height="50" fill="var(--navy)"/>
    </svg>
    <div class="logo-box">COMPANY lOGO</div>
    <div class="stamp-box">Stamp</div>
    <div class="company-details">
      <p>Details for your company</p>
      <p>Details for your company</p>
    </div>
    <div class="address-lines">
      <span></span><span></span><span></span><span></span><span></span><span></span>
    </div>
    <p class="contact-bar">Contact details: 1234567890 1234567890 www.ledgr.co</p>
  </section>

</main>
</body>
</html>
```